Project Sign for Construction Company

Site contractor needs a 4'x8' sign to place on construction sites for advertising. Our company builds the infrastructure for new housing developments. These sign will be posted on the road side to be viewed by passing cars. I want a clean and bold look and feel that resembles my company logo.

Font styles to use
Other font styles liked:
• Hypatia Sans Pro

Colors

Designer to choose colors to be used in the design.

Requirements
Must have
• 555-382-9146 | Info@MarlowPaving.example
• CUC 8047319
• www.MarlowPaving.example
• Services
• Road Construction
• Site Preparation & Excavation
• Underground Utilities
• Shoreline Restoration
Nice to have
• Now Hiring
• Pipe Layers
• Foremen
• Equipment Operators
Should not have
• Should not have stock picture images used in the design, focus on logo and geometric shapes

```html
<!DOCTYPE html>
<html lang="en">
<head>
<meta charset="utf-8">
<title>Marlow Paving – Roadside Site Sign</title>
<link rel="stylesheet" href="https://fonts.googleapis.com/css2?family=Cabin:wght@500;600;700&display=swap">
<style>
  :root {
    --brand-blue: #0550a0;
    --ink-blue: #0d4a94;
    --brand-green: #9ccc35;
    --white: #ffffff;
    --backdrop: #ececec;
    --band-grey: #dcdcdc;
  }
  * { margin: 0; padding: 0; box-sizing: border-box; }
  html, body { width: 1200px; height: 1200px; overflow: hidden; }
  body {
    background: var(--backdrop);
    font-family: "Cabin", "Trebuchet MS", sans-serif;
    position: relative;
  }
  .site-sign {
    position: absolute;
    left: 343px; top: 85px;
    width: 514px; height: 1030px;
    background: var(--white);
    overflow: hidden;
  }
  .sign-shapes { position: absolute; inset: 0; }
  .brand-name {
    position: absolute;
    top: 236px; left: 0; width: 100%;
    text-align: center;
    color: var(--white);
    font-weight: 700;
    font-size: 40px;
    letter-spacing: 2px;
  }
  .services-list {
    position: absolute;
    left: 37px; top: 436px;
    list-style: none;
    color: var(--ink-blue);
    font-weight: 700;
    font-size: 23.5px;
    letter-spacing: 0.3px;
  }
  .services-list li {
    height: 37px; line-height: 37px;
    position: relative;
    padding-left: 23px;
  }
  .services-list li::before {
    content: "";
    position: absolute; left: 0; top: 13px;
    width: 12px; height: 12px;
    border-radius: 50%;
    background: var(--ink-blue);
  }
  .hiring-tab {
    position: absolute;
    left: 41px; top: 645px;
    width: 433px; height: 76px;
    background: var(--brand-green);
    border-radius: 0 0 26px 26px;
    box-shadow: 0 4px 6px rgba(0,0,0,0.35);
    color: var(--white);
    font-weight: 700;
    font-size: 60px;
    line-height: 76px;
    text-align: center;
    letter-spacing: 1px;
  }
  .hiring-list {
    position: absolute;
    left: 35px; top: 740px;
    list-style: none;
    color: var(--white);
    font-weight: 700;
    font-size: 25px;
    letter-spacing: 0.3px;
  }
  .hiring-list li { height: 45px; line-height: 45px; }
  .contact-bar {
    position: absolute;
    left: 0; top: 925px;
    width: 100%; height: 45px;
    background: var(--brand-green);
    display: flex; align-items: center; justify-content: center;
    color: var(--white);
    font-weight: 500;
    font-size: 18.5px;
  }
  .contact-bar span { padding: 0 6px; }
  .contact-bar .divider {
    width: 2px; height: 30px; padding: 0;
    background: var(--white);
  }
  .web-address {
    position: absolute;
    left: 0; top: 984px;
    width: 100%;
    text-align: center;
    color: var(--white);
    font-weight: 600;
    font-size: 28px;
  }
</style>
</head>
<body>
  <div class="site-sign">
    <svg class="sign-shapes" width="514" height="1030" viewBox="0 0 514 1030">
      <polygon fill="var(--brand-blue)" points="0,0 514,0 514,272 258,398 0,272"/>
      <polygon fill="var(--band-grey)" points="514,272 258,398 205,424 252,448 514,320"/>
      <polygon fill="var(--brand-green)" points="0,272 258,398 205,424 0,326"/>
      <polygon fill="var(--brand-blue)" points="0,667 28,667 41,652 474,652 487,667 514,667 514,1030 0,1030"/>
    </svg>

    <div class="brand-name">MARLOW PAVING</div>

    <ul class="services-list">
      <li>SERVICES</li>
      <li>ROAD CONSTRUCTION</li>
      <li>UNDERGROUND UTILITIES</li>
      <li>SHORELINE RESTORATION</li>
      <li>SITE PREPARATION &amp; EXCAVATION</li>
    </ul>

    <div class="hiring-tab">NOW HIRING</div>

    <ul class="hiring-list">
      <li>ROAD CONSTRUCTION</li>
      <li>UNDERGROUND UTILITIES</li>
      <li>SITE PREPARATION &amp; EXCAVATION</li>
      <li>SHORELINE RESTORATION</li>
    </ul>

    <div class="contact-bar">
      <span>555-382-9146</span>
      <span class="divider"></span>
      <span>Info@MarlowPaving.example</span>
      <span class="divider"></span>
      <span>CUC 8047319</span>
    </div>

    <div class="web-address">www.MarlowPaving.example</div>
  </div>
</body>
</html>
```